BRELM - Letterhead

Willowmere Institute of Letters and Crafts (BRELM) is a non-profit organization that operates two tuition-free public schools - BRELM Elementary for grades K to 5th and BRELM College Prep for grades 6-12.

We are looking for a letterhead primarily to be used on Google Docs and Microsoft Word. Attached are two versions of our logo. One with our name spelled out and one with the acronym.

For Letterhead, we would like 3 addresses listed:

BRELM HQ
41872 Hollow Brook Lane, Suite 308
Fernhollow, CA 90412

BRELM Elementary (K-5)
18460 Marsh Ridge Boulevard
Fernhollow, CA 90412

BRELM College Prep (6-12)
27314 Del Sol Terrace
Marrow Bay Heights, CA 90438

Our Phone Number is (555) 418-7062
Our Fax Number is the same (555) 418-7062

Our website is www.brelmschools.org

Target Market(s)

Education

Industry/Entity Type

Education

Font styles to use
Sans Serif

Colors
0054AA
0677BA
7BADD7
CADEEF
E8F1F8

Requirements
Must have
• Logo, Address, Phone Number, Website.
Nice to have
• Modern and clean design.
Should not have
• Prefer that there is no bleed -- the letterhead will mostly be used in PDF format however sometimes it will be printed and our printers can not do a full bleed

```html
<!DOCTYPE html>
<html lang="en">
<head>
<meta charset="utf-8">
<title>BRELM – Letterhead Samples</title>
<link href="https://fonts.googleapis.com/css2?family=Figtree:ital,wght@0,400;0,500;0,600;0,700;1,400&display=swap" rel="stylesheet">
<style>
  :root{
    --backdrop:#808080;
    --label:#a6a6a6;
    --paper:#ffffff;
    --ink:#111111;
    --brand-navy:#1c3fa6;
    --brand-blue:#0677ba;
    --brand-sky:#1b86cf;
    --brand-red:#ee1c25;
    --bar-yellow:#f2c600;
    --bar-red:#ed1c24;
    --bar-orange:#f4663c;
    --bar-green:#1f9a3c;
    --bar-blue:#0b7dca;
    --bar-navy:#0b3ea5;
    --signature:#e4e6ea;
    --ghost:#f3f4f6;
    --font:"Figtree", Arial, sans-serif;
  }
  *{box-sizing:border-box;margin:0;padding:0}
  html,body{width:1200px;height:548px;overflow:hidden;background:var(--backdrop);font-family:var(--font);color:var(--ink)}
  .canvas{position:relative;width:1200px;height:548px}

  .sample-label{position:absolute;top:54px;writing-mode:vertical-rl;transform:rotate(180deg);
    font-size:8.5px;letter-spacing:.6px;color:var(--label);font-weight:400}

  .page{position:absolute;top:55px;width:318px;height:449px;background:var(--paper);overflow:hidden}
  .page--one{left:63px}
  .page--two{left:442px}
  .page--three{left:821px}

  .color-bar{position:absolute;left:0;width:100%;height:7px;
    background:linear-gradient(90deg,var(--bar-yellow) 0 16.66%,var(--bar-red) 16.66% 33.33%,var(--bar-orange) 33.33% 50%,var(--bar-green) 50% 66.66%,var(--bar-blue) 66.66% 83.33%,var(--bar-navy) 83.33% 100%)}
  .color-bar--bottom{bottom:0}
  .color-bar--top{top:0}
  .header-rule{position:absolute;left:22px;top:77px;width:273px;height:1px;
    background:linear-gradient(90deg,var(--bar-yellow) 0 16.66%,var(--bar-red) 16.66% 33.33%,var(--bar-orange) 33.33% 50%,var(--bar-green) 50% 66.66%,var(--bar-blue) 66.66% 83.33%,var(--bar-navy) 83.33% 100%)}

  .brand-mark{position:absolute;left:22px;display:flex;align-items:center;gap:4px}
  .brand-mark__dot{width:9px;height:9px;border-radius:50%;background:var(--brand-navy)}
  .brand-mark__name{font-size:17px;font-weight:600;color:var(--brand-navy);letter-spacing:.3px;line-height:1}

  .brand-wordmark{position:absolute;left:52px;top:30px;font-size:14px;font-weight:700;color:var(--brand-navy);line-height:17.5px;letter-spacing:-.1px}

  .header-contact{position:absolute;left:207px}
  .header-contact__org{font-size:6.6px;font-weight:500;color:var(--brand-navy);line-height:7.4px}
  .contact-list{list-style:none;margin-top:4.6px}
  .contact-list li{display:flex;align-items:center;gap:5px;font-size:5.2px;line-height:8.1px;color:var(--ink);white-space:nowrap}
  .icon{width:5px;height:5px;flex:none;fill:var(--brand-blue)}

  .recipient{position:absolute;left:35px;top:113px}
  .person__name{font-size:7.4px;font-weight:700;line-height:8px}
  .person__role{font-size:4.8px;font-style:italic;line-height:6px}

  .letter-body{position:absolute;left:34px;top:142px;width:255px}
  .letter-body p{font-size:4.55px;line-height:6.43px;text-align:justify;margin-bottom:6.43px}

  .signature{position:absolute;left:34px;top:320px;width:63px;height:30px;background:var(--signature)}
  .signer{position:absolute;left:35px;top:353px}
  .signer .person__name{font-weight:500}

  .ghost-mark{position:absolute;right:-6px;top:330px;font-size:56px;font-weight:700;color:var(--ghost);line-height:1;letter-spacing:1px}

  .addresses{position:absolute;left:0;width:100%}
  .address{position:absolute;display:flex;gap:4px}
  .address__pin{width:6px;height:7px;flex:none;margin-top:1px}
  .address__text{font-size:4.5px;line-height:6px;color:var(--ink);white-space:nowrap}
  .address__title{font-weight:600}
  .address--hq .address__title{color:var(--brand-red)}
  .address--hq .address__pin{fill:var(--brand-red)}
  .address--elem .address__title{color:var(--brand-sky)}
  .address--elem .address__pin{fill:var(--brand-sky)}
  .address--prep .address__title{color:var(--brand-navy)}
  .address--prep .address__pin{fill:var(--brand-navy)}
  .address--hq{left:20px}
  .address--elem{left:122px}
  .address--prep{left:216px}

  .footer-contact{position:absolute;left:20px;top:430px;display:flex;gap:5px;font-size:4.7px;align-items:center;white-space:nowrap}
  .footer-contact span{display:flex;align-items:center;gap:2.5px}
</style>
</head>
<body>
<div class="canvas">

  <svg width="0" height="0" style="position:absolute" aria-hidden="true">
    <defs>
      <symbol id="i-phone" viewBox="0 0 10 10"><path d="M2 0.5l2 2-1 1.3c.6 1.3 1.6 2.3 2.9 2.9L7.2 5.7l2 2L8 9.5C4 9.2.8 6 .5 2z"/></symbol>
      <symbol id="i-fax" viewBox="0 0 10 10"><path d="M2.5 0.5h5v2.5h-5zM0.5 3.5h9v4h-2v2h-5v-2h-2zM3.3 6.3v2.4h3.4V6.3z"/></symbol>
      <symbol id="i-mail" viewBox="0 0 10 10"><path d="M0.5 2h9v6h-9zM1.2 2.6L5 5.5l3.8-2.9"/></symbol>
      <symbol id="i-web" viewBox="0 0 10 10"><circle cx="5" cy="5" r="4.5"/><path d="M0.6 5h8.8M5 .5c-2.2 2.6-2.2 6.4 0 9M5 .5c2.2 2.6 2.2 6.4 0 9" stroke="#fff" stroke-width=".7" fill="none"/></symbol>
      <symbol id="i-pin" viewBox="0 0 12 14"><path d="M6 0l6 3.5v7L6 14 0 10.5v-7z"/><circle cx="6" cy="6.5" r="2.2" fill="#fff"/></symbol>
    </defs>
  </svg>

  <!-- Sample 1 -->
  <div class="sample-label" style="left:42px">SAMPLE 1</div>
  <section class="page page--one">
    <div class="brand-mark" style="top:47px"><span class="brand-mark__dot"></span><span class="brand-mark__name">BRELM</span></div>
    <div class="header-contact" style="top:19px">
      <div class="header-contact__org">Willowmere Institute<br>of Letters and Crafts</div>
      <ul class="contact-list">
        <li><svg class="icon"><use href="#i-phone"/></svg>Phone: (555) 418-7062</li>
        <li><svg class="icon"><use href="#i-fax"/></svg>Fax: (555) 418-7062</li>
        <li><svg class="icon"><use href="#i-mail"/></svg>Email: admissions@brelmschools.org</li>
        <li><svg class="icon"><use href="#i-web"/></svg>Visit: www.brelmschools.org</li>
      </ul>
    </div>
    <div class="header-rule"></div>

    <div class="recipient"><div class="person__name">Name Goes Here</div><div class="person__role">Designation here</div></div>
    <div class="letter-body">
      <p>Lorem Ipsum is simply dummy text of the printing and typesetting industry. Lorem Ipsum has been the industry's standard dummy text ever since the 1500s, when an unknown printer took a galley of type and scrambled it to make a type specimen book. It has survived not only five centuries, but also the leap into electronic typesetting, remaining essentially unchanged. It was popularised in the 1960s with the release of Letraset sheets containing Lorem Ipsum passages, and more recently with desktop publishing software like Aldus PageMaker including versions of Lorem Ipsum. Lorem Ipsum is simply dummy text of the printing and typesetting industry. Lorem Ipsum has been the industry's standard dummy text ever since the 1500s, when an unknown printer took a galley of type and scrambled it to make a type specimen book.</p>
      <p>Lorem Ipsum is simply dummy text of the printing and typesetting industry. Lorem Ipsum has been the industry's standard dummy text ever since the 1500s, when an unknown printer took a galley of type and scrambled it to make a type specimen book. It has survived not only five centuries, but also the leap into electronic typesetting, remaining essentially unchanged. It was popularised in the 1960s with the release of Letraset sheets containing Lorem Ipsum passages, and more recently with desktop publishing software like Aldus PageMaker including versions of Lorem Ipsum. Lorem Ipsum is simply dummy text of the printing and typesetting industry. Lorem Ipsum has been the industry's standard dummy text ever since the 1500s, when an unknown printer took a galley of type and scrambled it to make a type specimen book.</p>
      <p>Lorem Ipsum is simply dummy text of the printing and typesetting industry. Lorem Ipsum has been the industry's standard dummy text ever since the 1500s, when an unknown printer took a galley of type and scrambled it to make a type specimen book. It has survived not only five centuries, but also the leap into electronic typesetting, remaining essentially unchanged. It was popularised in the 1960s with the release of Letraset sheets containing Lorem Ipsum passages, and more recently with desktop publishing software like Aldus PageMaker including versions of Lorem Ipsum.</p>
    </div>
    <div class="signature" role="img" aria-label="Handwritten signature"></div>
    <div class="signer"><div class="person__name">Name Goes Here</div><div class="person__role">Designation here</div></div>

    <div class="addresses" style="top:418px">
      <div class="address address--hq"><svg class="address__pin"><use href="#i-pin"/></svg><div class="address__text"><div class="address__title">BRELM HQ</div>41872 Hollow Brook Lane, Suite 308<br>Fernhollow, CA 90412</div></div>
      <div class="address address--elem"><svg class="address__pin"><use href="#i-pin"/></svg><div class="address__text"><div class="address__title">BRELM Elementary (K-5)</div>18460 Marsh Ridge Boulevard<br>Fernhollow, CA 90412</div></div>
      <div class="address address--prep"><svg class="address__pin"><use href="#i-pin"/></svg><div class="address__text"><div class="address__title">BRELM College Prep (6-12)</div>27314 Del Sol Terrace<br>Marrow Bay Heights, CA 90438</div></div>
    </div>
    <div class="color-bar color-bar--bottom"></div>
  </section>

  <!-- Sample 2 -->
  <div class="sample-label" style="left:421px">SAMPLE 2</div>
  <section class="page page--two">
    <div class="color-bar color-bar--top"></div>
    <div class="ghost-mark" aria-hidden="true">BRELM</div>
    <div class="brand-mark" style="top:59px"><span class="brand-mark__dot"></span><span class="brand-mark__name">BRELM</span></div>
    <div class="header-contact" style="top:26px">
      <div class="header-contact__org">Willowmere Institute<br>of Letters and Crafts</div>
      <ul class="contact-list">
        <li><svg class="icon"><use href="#i-phone"/></svg>Phone: (555) 418-7062</li>
        <li><svg class="icon"><use href="#i-fax"/></svg>Fax: (555) 418-7062</li>
        <li><svg class="icon"><use href="#i-mail"/></svg>Email: admissions@brelmschools.org</li>
        <li><svg class="icon"><use href="#i-web"/></svg>Visit: www.brelmschools.org</li>
      </ul>
    </div>

    <div class="recipient"><div class="person__name">Name Goes Here</div><div class="person__role">Designation here</div></div>
    <div class="letter-body">
      <p>Lorem Ipsum is simply dummy text of the printing and typesetting industry. Lorem Ipsum has been the industry's standard dummy text ever since the 1500s, when an unknown printer took a galley of type and scrambled it to make a type specimen book. It has survived not only five centuries, but also the leap into electronic typesetting, remaining essentially unchanged. It was popularised in the 1960s with the release of Letraset sheets containing Lorem Ipsum passages, and more recently with desktop publishing software like Aldus PageMaker including versions of Lorem Ipsum. Lorem Ipsum is simply dummy text of the printing and typesetting industry. Lorem Ipsum has been the industry's standard dummy text ever since the 1500s, when an unknown printer took a galley of type and scrambled it to make a type specimen book.</p>
      <p>Lorem Ipsum is simply dummy text of the printing and typesetting industry. Lorem Ipsum has been the industry's standard dummy text ever since the 1500s, when an unknown printer took a galley of type and scrambled it to make a type specimen book. It has survived not only five centuries, but also the leap into electronic typesetting, remaining essentially unchanged. It was popularised in the 1960s with the release of Letraset sheets containing Lorem Ipsum passages, and more recently with desktop publishing software like Aldus PageMaker including versions of Lorem Ipsum. Lorem Ipsum is simply dummy text of the printing and typesetting industry. Lorem Ipsum has been the industry's standard dummy text ever since the 1500s, when an unknown printer took a galley of type and scrambled it to make a type specimen book.</p>
      <p>Lorem Ipsum is simply dummy text of the printing and typesetting industry. Lorem Ipsum has been the industry's standard dummy text ever since the 1500s, when an unknown printer took a galley of type and scrambled it to make a type specimen book. It has survived not only five centuries, but also the leap into electronic typesetting, remaining essentially unchanged. It was popularised in the 1960s with the release of Letraset sheets containing Lorem Ipsum passages, and more recently with desktop publishing software like Aldus PageMaker including versions of Lorem Ipsum.</p>
    </div>
    <div class="signature" role="img" aria-label="Handwritten signature"></div>
    <div class="signer"><div class="person__name">Name Goes Here</div><div class="person__role">Designation here</div></div>

    <div class="addresses" style="top:418px">
      <div class="address address--hq"><svg class="address__pin"><use href="#i-pin"/></svg><div class="address__text"><div class="address__title">BRELM HQ</div>41872 Hollow Brook Lane, Suite 308<br>Fernhollow, CA 90412</div></div>
      <div class="address address--elem"><svg class="address__pin"><use href="#i-pin"/></svg><div class="address__text"><div class="address__title">BRELM Elementary (K-5)</div>18460 Marsh Ridge Boulevard<br>Fernhollow, CA 90412</div></div>
      <div class="address address--prep"><svg class="address__pin"><use href="#i-pin"/></svg><div class="address__text"><div class="address__title">BRELM College Prep (6-12)</div>27314 Del Sol Terrace<br>Marrow Bay Heights, CA 90438</div></div>
    </div>
    <div class="color-bar color-bar--bottom"></div>
  </section>

  <!-- Sample 3 -->
  <div class="sample-label" style="left:800px">SAMPLE 3</div>
  <section class="page page--three">
    <div class="brand-wordmark">Willowmere Institute of Letters<br>and Crafts</div>

    <div class="recipient"><div class="person__name">Name Goes Here</div><div class="person__role">Designation here</div></div>
    <div class="letter-body">
      <p>Lorem Ipsum is simply dummy text of the printing and typesetting industry. Lorem Ipsum has been the industry's standard dummy text ever since the 1500s, when an unknown printer took a galley of type and scrambled it to make a type specimen book. It has survived not only five centuries, but also the leap into electronic typesetting, remaining essentially unchanged. It was popularised in the 1960s with the release of Letraset sheets containing Lorem Ipsum passages, and more recently with desktop publishing software like Aldus PageMaker including versions of Lorem Ipsum. Lorem Ipsum is simply dummy text of the printing and typesetting industry. Lorem Ipsum has been the industry's standard dummy text ever since the 1500s, when an unknown printer took a galley of type and scrambled it to make a type specimen book.</p>
      <p>Lorem Ipsum is simply dummy text of the printing and typesetting industry. Lorem Ipsum has been the industry's standard dummy text ever since the 1500s, when an unknown printer took a galley of type and scrambled it to make a type specimen book. It has survived not only five centuries, but also the leap into electronic typesetting, remaining essentially unchanged. It was popularised in the 1960s with the release of Letraset sheets containing Lorem Ipsum passages, and more recently with desktop publishing software like Aldus PageMaker including versions of Lorem Ipsum. Lorem Ipsum is simply dummy text of the printing and typesetting industry. Lorem Ipsum has been the industry's standard dummy text ever since the 1500s, when an unknown printer took a galley of type and scrambled it to make a type specimen book.</p>
      <p>Lorem Ipsum is simply dummy text of the printing and typesetting industry. Lorem Ipsum has been the industry's standard dummy text ever since the 1500s, when an unknown printer took a galley of type and scrambled it to make a type specimen book. It has survived not only five centuries, but also the leap into electronic typesetting, remaining essentially unchanged. It was popularised in the 1960s with the release of Letraset sheets containing Lorem Ipsum passages, and more recently with desktop publishing software like Aldus PageMaker including versions of Lorem Ipsum.</p>
    </div>
    <div class="signature" role="img" aria-label="Handwritten signature"></div>
    <div class="signer"><div class="person__name">Name Goes Here</div><div class="person__role">Designation here</div></div>

    <div class="addresses" style="top:406px">
      <div class="address address--hq" style="left:21px"><svg class="address__pin"><use href="#i-pin"/></svg><div class="address__text"><div class="address__title">BRELM HQ</div>41872 Hollow Brook Lane, Suite 308<br>Fernhollow, CA 90412</div></div>
      <div class="address address--elem" style="left:123px"><svg class="address__pin"><use href="#i-pin"/></svg><div class="address__text"><div class="address__title">BRELM Elementary (K-5)</div>18460 Marsh Ridge Boulevard<br>Fernhollow, CA 90412</div></div>
      <div class="address address--prep" style="left:217px"><svg class="address__pin"><use href="#i-pin"/></svg><div class="address__text"><div class="address__title">BRELM College Prep (6-12)</div>27314 Del Sol Terrace<br>Marrow Bay Heights, CA 90438</div></div>
    </div>
    <div class="footer-contact">
      <span><svg class="icon"><use href="#i-phone"/></svg>Phone: (555) 418-7062</span>
      <span><svg class="icon"><use href="#i-fax"/></svg>Fax: (555) 418-7062</span>
      <span><svg class="icon"><use href="#i-mail"/></svg>Email: admissions@brelmschools.org</span>
      <span><svg class="icon"><use href="#i-web"/></svg>Visit: www.brelmschools.org</span>
    </div>
    <div class="color-bar color-bar--bottom"></div>
  </section>

</div>
</body>
</html>
```